Website design for Meridian Tote printing specialist

We need an overhaul of our website front end design. We need a new look and a modern take on the products we sell and service we offer. We sell plain stock in a variety of bag types and offer a printing service of customers branding and logos. Customers request online quotes and this facility must be an easy one step process for users. Our logo is currently green and orange and we are not really looking for re branding at this stage. The final design must communicate that we are the leading printing specialist throughout the country, have been in operation for 15 years and have a vast amount of experience and expertise. The design must instantly show the products available and the ability to request a quote for the desired product.

Target Market(s)

Trade shows, retailers, dentists, food suppliers. wine makers etc etc and anyone that uses carry bags

Industry/Entity Type

Screen Printing

Number of Pages Required

5+ page

Font styles to use
Serif
Sans Serif

Colors

Designer to choose colors to be used in the design.

Requirements
Must have
• Our home page featuring all the products as selectable entities and a short description of what each bag type is when the user hovers over the image.
• Then the product landing pages must show different sizes of that product type. On each page there must be a quick quote button that goes to the quote screen with the features and information to select or include for a quote to be processed. The logo is green and orange and still should have this present but happy to move away from this on the website pages in general.I have so many product pictures and unable to upload them all here. The categories for products are as follows:
• Kraft Paper Bags
• Laminated bags
• Non-woven bags
• Calico bags
• Wine bags
• Florist bags
• Plastic Bags
• Printed Bags
• Gift Boxes
• Tissue paper
• Wrapping Paper
• Custom Bags and Boxes
• There also needs to be a gallery page that showcases work we have done. The ability to have a description for each photo in the gallery would be great.
• A general bag size page would be great and one content page that is about us and another for contact us.
• A free sample button so a user can request a sample. Phone number must be included on this page and unable to submit with a valid phone number.
• Our phone number should be prominent.
• A search feature please.
Nice to have
• Fonts should be in keeping with the design of the website
Should not have
• I dont want users having to scroll too far down to find information. The icons of the bags on the home screen should almost appear on one screen.
• I can upload all my content and pictures so no need to get them from me. I really want your look and feel and design layout that i can then work from.

```html
<!DOCTYPE html>
<html lang="en">
<head>
<meta charset="utf-8">
<title>Meridian Tote – Printed Bags</title>
<link href="https://fonts.googleapis.com/css2?family=Roboto+Condensed:wght@400;700&family=Montserrat:wght@400;600&family=Satisfy&display=swap" rel="stylesheet">
<style>
:root{
  --green:#7dc142;
  --green-dark:#5b9a2f;
  --orange:#f47f20;
  --black:#0e0e0e;
  --ink:#1d1d1d;
  --text:#555;
  --grey:#e9e9e9;
  --field:#eeeeee;
  --footer:#efefef;
  --white:#fff;
  --navy:#1f4f7a;
}
*{box-sizing:border-box;margin:0;padding:0}
html,body{width:1200px;height:3666px;overflow:hidden}
body{position:relative;background:var(--white);font-family:"Montserrat",sans-serif;color:var(--text)}
.abs{position:absolute}

/* header */
.topbar{left:0;top:0;width:1200px;height:64px;background:var(--black)}
.search{left:78px;top:10px;width:290px;height:42px;border-radius:21px;background:#2a2a2a;color:#888;font-size:14px;line-height:42px;padding-left:22px}
.phone{right:80px;top:0;height:64px;display:flex;align-items:center;gap:10px;color:var(--white);font-family:"Roboto Condensed",sans-serif;font-weight:700;font-size:24px}
.navbar{left:0;top:64px;width:1200px;height:58px;background:var(--green)}
.nav a{position:absolute;top:64px;line-height:58px;color:var(--white);font-family:"Roboto Condensed",sans-serif;font-weight:700;font-size:18px;text-decoration:none}
.logo-tab{left:477px;top:0;width:244px;height:150px}
.brand{left:477px;top:50px;width:244px;text-align:center;font-family:"Roboto Condensed",sans-serif;font-weight:700;font-size:30px;color:var(--green)}

/* hero */
.hero{left:39px;top:142px;width:1122px;height:540px;
  background:
    linear-gradient(180deg,rgba(0,0,0,0) 55%,rgba(120,60,70,.35) 100%),
    linear-gradient(100deg,#2f2f2f 0%,#6f6f6f 35%,#9a9a9a 55%,#5c5c5c 80%,#3a3a3a 100%)}
.hero-title{left:110px;top:282px;color:var(--white);font-family:"Roboto Condensed",sans-serif;font-weight:700}
.hero-title .l1{display:block;font-size:48px;line-height:56px;font-weight:400}
.hero-title .l2{display:block;font-size:80px;line-height:86px}
.hero-title .l3{display:block;font-family:"Satisfy",cursive;font-weight:400;color:var(--orange);font-size:84px;line-height:82px;margin-left:6px}
.dots{left:1106px;top:322px}

/* features */
.features{left:39px;top:687px;width:1122px;height:149px;background:var(--grey);display:flex}
.feature{flex:1;display:flex;flex-direction:column;align-items:center;justify-content:center;gap:14px;border-left:6px solid var(--white);font-family:"Roboto Condensed",sans-serif;font-weight:700;font-size:17px;color:var(--ink)}
.feature:first-child{border-left:none}

/* products */
.section-title{width:1200px;left:0;text-align:center;font-family:"Roboto Condensed",sans-serif;font-weight:400;font-size:42px;color:var(--ink)}
.intro{left:250px;width:700px;top:980px;text-align:center;font-size:13px;line-height:27px}
.card{width:242px;height:250px;box-shadow:0 4px 14px rgba(0,0,0,.18)}
.pname{width:242px;text-align:center;font-family:"Roboto Condensed",sans-serif;font-weight:700;font-size:17px;color:var(--ink)}
.psub{width:242px;text-align:center;font-size:13px;color:#333}
.price{width:242px;text-align:center;font-family:"Roboto Condensed",sans-serif;font-weight:700;font-size:26px;color:var(--green)}
.btn{display:block;text-align:center;border-radius:26px;font-family:"Roboto Condensed",sans-serif;font-weight:700;color:var(--white);background:var(--orange);text-decoration:none}
.btn-ghost{background:var(--white);color:var(--orange);border:2px solid var(--orange)}

/* promo band */
.band{left:0;top:1997px;width:1200px;height:362px;background:linear-gradient(90deg,#6aa93a,var(--green-dark))}
.promo-photo{left:37px;top:1975px;width:623px;height:384px;background:linear-gradient(90deg,#c94a3a 0%,#e9b060 35%,#e7c9b4 55%,#e76aa2 78%,#c8d85a 100%)}
.promo-lead{left:697px;top:2105px;color:var(--white);font-family:"Roboto Condensed",sans-serif;font-size:20px}
.promo-head{left:697px;top:2142px;color:var(--white);font-family:"Roboto Condensed",sans-serif;font-weight:700;font-size:28px;line-height:32px}

/* about + contact */
.h2{font-family:"Roboto Condensed",sans-serif;font-weight:400;font-size:42px;color:var(--ink)}
.about-sub{left:78px;top:2503px;color:var(--orange);font-family:"Roboto Condensed",sans-serif;font-weight:700;font-size:18px}
.about-p{left:78px;width:480px;font-size:13px;line-height:28px}
.field{background:var(--field);font-size:13px;color:#666;padding:14px 16px}

/* testimonials */
.testi{left:0;top:2903px;width:1200px;height:448px;background:var(--orange)}
.avatar{left:455px;top:3043px;width:80px;height:80px;border-radius:50%;background:linear-gradient(160deg,#7a6a5e,#3c4f60)}
.client{left:552px;top:3055px;color:var(--white);font-family:"Roboto Condensed",sans-serif;font-weight:700;font-size:18px}
.client-sub{left:552px;top:3094px;color:var(--white);font-size:12px}
.quote{left:210px;width:780px;top:3152px;text-align:center;color:var(--white);font-size:12.5px;line-height:26px}

/* footer */
.footer{left:0;top:3351px;width:1200px;height:315px;background:var(--footer)}
.f-brand{left:112px;top:3420px;font-family:"Roboto Condensed",sans-serif;font-weight:700;font-size:34px;color:var(--green)}
.social{left:110px;top:3495px;display:flex;gap:10px}
.social span{width:40px;height:40px;border-radius:50%;background:var(--navy)}
.f-col{top:3380px}
.f-col h4{font-family:"Roboto Condensed",sans-serif;font-weight:700;font-size:18px;color:var(--ink);margin-bottom:10px}
.f-col p{font-size:13px;line-height:29px;color:#555}
.f-rule{left:78px;top:3597px;width:1044px;height:1px;background:#d6d6d6}
.copy{left:0;width:1200px;top:3618px;text-align:center;font-size:12px;color:#444}
</style>
</head>
<body>

<!-- header -->
<div class="abs topbar"></div>
<div class="abs search">Search</div>
<div class="abs phone">
  <svg width="24" height="24" viewBox="0 0 24 24"><path d="M6.6 10.8a15 15 0 0 0 6.6 6.6l2.2-2.2a1 1 0 0 1 1-.25 11.4 11.4 0 0 0 3.6.57 1 1 0 0 1 1 1V20a1 1 0 0 1-1 1A17 17 0 0 1 3 4a1 1 0 0 1 1-1h3.5a1 1 0 0 1 1 1c0 1.25.2 2.45.57 3.57a1 1 0 0 1-.25 1z" fill="#7dc142"/></svg>
  +91-555-010-2040
</div>
<div class="abs navbar"></div>
<nav class="nav">
  <a style="left:184px">HOME</a>
  <a style="left:265px">SHOP</a>
  <a style="left:350px">GALLERY</a>
  <a style="left:737px">ABOUT US</a>
  <a style="left:856px">CONTACT US</a>
  <a style="left:995px">LOGIN</a>
</nav>
<svg class="abs logo-tab" viewBox="0 0 244 150"><polygon points="0,0 244,0 244,110 122,150 0,110" fill="#fff"/></svg>
<div class="abs brand">Meridian Tote</div>

<!-- hero -->
<div class="abs hero" role="img" aria-label="Photo: black and white city street with a woman in a hat carrying colourful shopping bags"></div>
<h1 class="abs hero-title"><span class="l1">CHOOSE YOUR</span><span class="l2">FAVOURITE</span><span class="l3">style</span></h1>
<svg class="abs dots" width="28" height="180" viewBox="0 0 28 180">
  <g fill="none" stroke="#fff" stroke-width="2">
    <circle cx="14" cy="8" r="6"/><circle cx="14" cy="32" r="6"/>
    <circle cx="14" cy="150" r="6"/><circle cx="14" cy="172" r="6"/>
    <line x1="14" y1="70" x2="14" y2="138"/>
  </g>
  <circle cx="14" cy="56" r="7" fill="#f47f20"/>
</svg>

<!-- features -->
<div class="abs features">
  <div class="feature">
    <svg width="46" height="40" viewBox="0 0 46 40" fill="none" stroke="#222" stroke-width="2.5"><rect x="3" y="8" width="40" height="28" rx="3"/><path d="M8 8 30 2l4 6"/><rect x="30" y="17" width="13" height="10"/></svg>
    MONEY BACK GUARANTEE
  </div>
  <div class="feature">
    <svg width="50" height="40" viewBox="0 0 50 40" fill="none" stroke="#222" stroke-width="2.5" stroke-linejoin="round"><path d="M4 20 46 4 34 36 24 24z M24 24 46 4 M14 22l-6 10 10-4"/></svg>
    FAST SHIPPING
  </div>
  <div class="feature">
    <svg width="46" height="40" viewBox="0 0 46 40" fill="none" stroke="#222" stroke-width="2.5" stroke-linejoin="round"><path d="M12 3h22l9 11-20 23L3 14z M3 14h40 M17 3l6 11 6-11 M15 14l8 23 8-23"/></svg>
    PRODUCT QUALITY
  </div>
  <div class="feature">
    <svg width="42" height="42" viewBox="0 0 42 42" fill="none" stroke="#222" stroke-width="2.5"><circle cx="21" cy="15" r="9"/><path d="M9 15a12 12 0 0 1 24 0 M6 40c1-10 8-14 15-14s14 4 15 14 M30 22l-6 2"/></svg>
    ONLINE SUPPORT
  </div>
</div>

<!-- featured products -->
<h2 class="abs section-title" style="top:922px">FEATURED PRODUCTS</h2>
<p class="abs intro">Lorem Ipsum is simply dummy text of the printing and typesetting industry. Lorem Ipsum has been the industry's standard dummy text ever since the hen an unknown.</p>

<!-- row 1 -->
<div class="abs card" style="left:78px;top:1088px;background:radial-gradient(circle at 50% 50%,#ece9e4 0%,#fff 65%)" role="img" aria-label="Product photo: white wine bag">
  <a class="abs btn" style="left:43px;top:84px;width:155px;height:46px;line-height:46px;font-size:17px">ADD TO CART</a>
  <a class="abs btn btn-ghost" style="left:43px;top:143px;width:155px;height:46px;line-height:42px;font-size:17px">QUICK QUOTE</a>
</div>
<div class="abs card" style="left:347px;top:1088px;background:radial-gradient(circle at 50% 55%,#f6a6cb 0%,#fff 70%)" role="img" aria-label="Product photo: pink laminated bag"></div>
<div class="abs card" style="left:613px;top:1088px;background:radial-gradient(circle at 50% 50%,#e6dfd6 0%,#fff 68%)" role="img" aria-label="Product photo: white bottle carrier box"></div>
<div class="abs card" style="left:880px;top:1088px;background:radial-gradient(circle at 50% 50%,#f4b3ba 0%,#fff 68%)" role="img" aria-label="Product photo: pink pillow box"></div>
<div class="abs pname" style="left:78px;top:1360px">WINE BAGS</div>
<div class="abs pname" style="left:347px;top:1360px">LAMINATED BAGS</div>
<div class="abs pname" style="left:613px;top:1360px">TISSUE PAPER</div>
<div class="abs pname" style="left:880px;top:1360px">CALICO BAGS</div>
<div class="abs psub" style="left:78px;top:1387px">Lorem ipsum is simple text</div>
<div class="abs psub" style="left:347px;top:1387px">Lorem ipsum is simple text</div>
<div class="abs psub" style="left:613px;top:1387px">Lorem ipsum is simple text</div>
<div class="abs psub" style="left:880px;top:1387px">Lorem ipsum is simple text</div>
<div class="abs price" style="left:78px;top:1414px">$35.00</div>
<div class="abs price" style="left:347px;top:1414px">$35.00</div>
<div class="abs price" style="left:613px;top:1414px">$35.00</div>
<div class="abs price" style="left:880px;top:1414px">$35.00</div>

<!-- row 2 -->
<div class="abs card" style="left:78px;top:1505px;background:radial-gradient(circle at 50% 50%,#d78a91 0%,#fff 66%)" role="img" aria-label="Product photo: red wine bag"></div>
<div class="abs card" style="left:347px;top:1505px;background:radial-gradient(circle at 50% 55%,#c9c8c0 0%,#fff 70%)" role="img" aria-label="Product photo: grey gift box"></div>
<div class="abs card" style="left:613px;top:1505px;background:radial-gradient(circle at 50% 55%,#f7c6e2 0%,#fff 68%)" role="img" aria-label="Product photo: pink non-woven tote bag"></div>
<div class="abs card" style="left:880px;top:1505px;background:radial-gradient(circle at 50% 55%,#d3bc98 0%,#e6f0e4 45%,#fff 72%)" role="img" aria-label="Product photo: jute bag with green trim"></div>
<div class="abs pname" style="left:78px;top:1778px">WINE BAGS</div>
<div class="abs pname" style="left:347px;top:1778px">LAMINATED BAGS</div>
<div class="abs pname" style="left:613px;top:1778px">TISSUE PAPER</div>
<div class="abs pname" style="left:880px;top:1778px">CALICO BAGS</div>
<div class="abs psub" style="left:78px;top:1805px">Lorem ipsum is simple text</div>
<div class="abs psub" style="left:347px;top:1805px">Lorem ipsum is simple text</div>
<div class="abs psub" style="left:613px;top:1805px">Lorem ipsum is simple text</div>
<div class="abs psub" style="left:880px;top:1805px">Lorem ipsum is simple text</div>
<div class="abs price" style="left:78px;top:1833px">$35.00</div>
<div class="abs price" style="left:347px;top:1833px">$35.00</div>
<div class="abs price" style="left:613px;top:1833px">$35.00</div>
<div class="abs price" style="left:880px;top:1833px">$35.00</div>

<!-- promo band -->
<div class="abs band"></div>
<div class="abs promo-photo" role="img" aria-label="Photo: smiling woman holding bright shopping bags over her shoulder"></div>
<p class="abs promo-lead">We Sell Plain Stock In A Variety Of Bag Types And</p>
<p class="abs promo-head">OFFER A PRINTING SERVICE OF<br>CUSTOMERS BRANDING AND LOGOS</p>
<a class="abs btn" style="left:704px;top:2226px;width:213px;height:50px;line-height:50px;font-size:18px">GET ONLINE QUOTE</a>

<!-- about -->
<h2 class="abs h2" style="left:78px;top:2438px">ABOUT US</h2>
<p class="abs about-sub">LOREM IPSUM IS SIMPLY DUMMY TEXT OF THE PRINTING.</p>
<p class="abs about-p" style="top:2536px">Lorem Ipsum is simply dummy text of the printing and typesetting industry. Lorem Ipsum has been the industry's standard dummy text ever since the 1500s, when an unknown printer took a galley of type and scrambled it to make a type specimen book.</p>
<p class="abs about-p" style="top:2668px">It has survived not only five centuries, but also the leap into electronic typesetting, remaining essentially unchanged.</p>
<a class="abs btn" style="left:78px;top:2757px;width:152px;height:44px;line-height:44px;font-size:16px;background:var(--green)">READ MORE</a>

<!-- contact -->
<h2 class="abs h2" style="left:609px;top:2438px">CONTACT US</h2>
<div class="abs field" style="left:609px;top:2510px;width:246px;height:49px">Name</div>
<div class="abs field" style="left:873px;top:2510px;width:249px;height:49px">Contact No.</div>
<div class="abs field" style="left:609px;top:2576px;width:513px;height:51px">Email</div>
<div class="abs field" style="left:609px;top:2645px;width:513px;height:112px">Message</div>
<a class="abs btn" style="left:609px;top:2776px;width:151px;height:44px;line-height:44px;font-size:16px;background:var(--green)">SUBMIT</a>

<!-- testimonials -->
<div class="abs testi"></div>
<h2 class="abs section-title" style="top:2980px;color:var(--white)">CLIENTS TESTIMONIALS</h2>
<div class="abs avatar" role="img" aria-label="Client portrait photo"></div>
<p class="abs client">- CLIENT NAME</p>
<p class="abs client-sub">Lorem ipsum is simply dummy</p>
<p class="abs quote">Lorem Ipsum is simply dummy text of the printing and typesetting industry. Lorem Ipsum has been the industry's standard dummy text ever since the 1500s, when an unknown printer took a galley of type and scrambled it to make a type specimen book. It has survived not only five centuries, but also the leap into electronic typesetting.</p>
<svg class="abs" style="left:562px;top:3252px" width="76" height="22" viewBox="0 0 76 22" fill="none" stroke="#fff" stroke-width="2.5" stroke-linecap="round" stroke-linejoin="round"><path d="M30 11H4m8-8-8 8 8 8 M46 11h26m-8-8 8 8-8 8"/></svg>

<!-- footer -->
<div class="abs footer"></div>
<div class="abs f-brand">Meridian Tote</div>
<div class="abs social"><span></span><span></span><span></span><span></span></div>
<div class="abs f-col" style="left:354px"><h4>SITEMAP</h4><p>Home<br>Products<br>Gallery<br>About<br>Contact Us</p></div>
<div class="abs f-col" style="left:540px"><h4>COMPANY INFO</h4><p>About The Founder<br>Email: info@meridiantote.com<br>Phone: 555 010 2040<br>Newsletter</p></div>
<div class="abs f-col" style="left:745px"><h4>SHOP WITH US</h4><p>View Cart<br>My Account<br>Order Traking</p></div>
<div class="abs f-col" style="left:943px"><h4>HELPFULL INFO</h4><p>Help/Faq<br>Privacy Policy<br>Terms &amp; Conditions</p></div>
<div class="abs f-rule"></div>
<p class="abs copy">©Meridian Tote - 2019 All Rights Reserved.</p>

</body>
</html>
```